Vornel Technologies business card design

We need a business card designed with our new logo. it would be great if the card could communicate it is a technology based company.

Target Market(s)

system integrators

Industry/Entity Type

technology, IOT

Contact Information for Business Card

Name, designation, Address, telephone number, email address

Requirements
Must have
• logo and company name
Nice to have
• something to do with technology

```html
<!DOCTYPE html>
<html lang="en">
<head>
<meta charset="utf-8">
<title>Vornel Technologies – Business Card</title>
<link href="https://fonts.googleapis.com/css2?family=Montserrat:wght@400;500;700&display=swap" rel="stylesheet">
<style>
  :root {
    --stage: #3a3b3e;
    --card-dark: #3d3d40;
    --card-light: #ffffff;
    --accent: #f28c1c;
    --text-light: #ffffff;
    --text-dark: #3d3d40;
  }
  * { box-sizing: border-box; margin: 0; padding: 0; }
  html, body {
    width: 1200px; height: 887px; overflow: hidden;
    background: var(--stage);
    font-family: "Montserrat", sans-serif;
  }
  .stage {
    position: relative; width: 1200px; height: 887px;
    display: flex; align-items: center; justify-content: center; gap: 40px;
  }
  .card {
    position: relative; width: 540px; height: 309px;
    border-radius: 22px; overflow: hidden;
  }
  .card-front { background: var(--card-dark); display: flex; align-items: center; justify-content: center; }
  .card-back { background: var(--card-light); }
  .brand {
    display: flex; align-items: center; gap: 12px;
    font-weight: 700; letter-spacing: 1px; text-transform: uppercase; line-height: 1.05;
  }
  .brand-mark { width: 34px; height: 34px; background: var(--accent); flex: none; }
  .brand-front { color: var(--text-light); font-size: 32px; }
  .brand-back {
    position: absolute; top: 30px; right: 50px;
    color: var(--text-dark); font-size: 19px;
  }
  .brand-back .brand-mark { width: 24px; height: 24px; }
  .wave { position: absolute; inset: 0; width: 100%; height: 100%; }
  .details {
    position: absolute; left: 132px; top: 166px;
    color: var(--text-light); font-size: 11px; line-height: 14px;
  }
  .person-name { color: var(--accent); font-weight: 700; font-size: 15px; line-height: 19px; letter-spacing: .3px; }
  .person-role { margin-bottom: 6px; }
  .address { margin-bottom: 6px; }
  .contact-list { list-style: none; }
  .contact-list li { display: flex; align-items: center; gap: 8px; height: 15px; }
  .contact-list svg { width: 11px; height: 11px; flex: none; }
</style>
</head>
<body>
<main class="stage">
  <section class="card card-front">
    <div class="brand brand-front">
      <span class="brand-mark"></span>
      <span>Vornel<br>Technologies</span>
    </div>
  </section>

  <section class="card card-back">
    <svg class="wave" viewBox="0 0 540 309" preserveAspectRatio="none" aria-hidden="true">
      <path d="M55,309 C45,180 80,150 200,150 C330,150 510,145 528,50 L540,50 L540,309 Z" fill="var(--card-dark)"/>
      <path d="M44,262 C50,170 85,141 200,141 C330,141 505,136 520,50" fill="none" stroke="var(--accent)" stroke-width="4.5"/>
    </svg>

    <div class="brand brand-back">
      <span class="brand-mark"></span>
      <span>Vornel<br>Technologies</span>
    </div>

    <div class="details">
      <p class="person-name">DALEN WHITCOMBE</p>
      <p class="person-role">Co-Founder</p>
      <p class="address">Halvern Tower 2210 Crest Avenue<br>Suite 118</p>
      <ul class="contact-list">
        <li>
          <svg viewBox="0 0 24 24"><path fill="var(--accent)" d="M6.6 10.8a15 15 0 0 0 6.6 6.6l2.2-2.2c.3-.3.7-.4 1-.2 1.1.4 2.3.6 3.6.6.6 0 1 .4 1 1V20c0 .6-.4 1-1 1C10.6 21 3 13.4 3 4c0-.6.4-1 1-1h3.5c.6 0 1 .4 1 1 0 1.3.2 2.5.6 3.6.1.3 0 .7-.2 1z"/></svg>
          <span>555-014-7732</span>
        </li>
        <li>
          <svg viewBox="0 0 24 24"><path fill="var(--accent)" d="M2 5h20v14H2z"/><path d="M2 5l10 8 10-8" fill="none" stroke="var(--card-dark)" stroke-width="2"/></svg>
          <span>info@vornel.com</span>
        </li>
        <li>
          <svg viewBox="0 0 24 24"><circle cx="12" cy="12" r="10" fill="var(--accent)"/><path d="M2 12h20M12 2c3 3 3 17 0 20M12 2c-3 3-3 17 0 20" fill="none" stroke="var(--card-dark)" stroke-width="1.5"/></svg>
          <span>www.vornel.com</span>
        </li>
      </ul>
    </div>
  </section>
</main>
</body>
</html>
```